Children's martial arts flyer for new classes

Need a postcard flyer addressing the attached spec (see file).

Flyer needs to be Postcard Size and be suited in style to the target demographic which is parents of children aged 5-12 years old.

Classes are new.

Postcard must include the logo and a picture. I have included an example pic in the attached file, but feel free to use other suitable pics.

Target Market(s)

Parents with children aged 5-12 years old

Colors

Designer to choose colors to be used in the design.

Requirements
Must have
• clean look.
• professional.

```html
<!DOCTYPE html>
<html lang="en">
<head>
<meta charset="utf-8">
<title>Children's Martial Art Classes Flyer</title>
<link rel="stylesheet" href="https://fonts.googleapis.com/css2?family=Archivo+Black&family=Michroma&family=Roboto+Condensed:wght@700&family=Arimo&display=swap">
<style>
  :root {
    --stage: #8c8c8c;
    --red: #e21f26;
    --dark: #282828;
    --yellow: #fbb829;
    --orange: #f08a24;
    --white: #ffffff;
    --photo-light: #eceff1;
    --photo-mid: #c9ced3;
    --map-fill: #e8e4d6;
  }
  html, body {
    margin: 0;
    width: 1200px;
    height: 1200px;
    overflow: hidden;
    background: var(--stage);
  }
  .flyer {
    position: absolute;
    left: 175px;
    top: 47px;
    width: 850px;
    height: 1105px;
    overflow: hidden;
    background: var(--dark);
  }
  .flyer-shapes {
    position: absolute;
    inset: 0;
  }
  .brand {
    position: absolute;
    left: 40px;
    top: 140px;
    display: flex;
    align-items: center;
    gap: 14px;
  }
  .brand-dot {
    width: 72px;
    height: 72px;
    border-radius: 50%;
    background: var(--yellow);
    flex: none;
  }
  .brand-name {
    font-family: "Archivo Black", sans-serif;
    font-size: 28px;
    color: var(--dark);
    letter-spacing: 1px;
  }
  .headline {
    position: absolute;
    left: 36px;
    top: 356px;
    color: var(--white);
    margin: 0;
    font-weight: normal;
  }
  .headline-small {
    display: block;
    font-family: "Michroma", sans-serif;
    font-size: 31px;
    line-height: 44px;
    font-weight: bold;
  }
  .headline-big {
    display: block;
    font-family: "Archivo Black", sans-serif;
    font-size: 62px;
    line-height: 66px;
  }
  .headline-mid {
    display: block;
    font-family: "Archivo Black", sans-serif;
    font-size: 48px;
    line-height: 64px;
    margin-left: -4px;
  }
  .tagline {
    position: absolute;
    left: 36px;
    top: 595px;
    margin: 0;
    font-family: "Archivo Black", sans-serif;
    font-size: 36px;
    line-height: 50px;
    color: var(--white);
  }
  .schedule {
    position: absolute;
    left: 36px;
    top: 727px;
    margin: 0;
    font-family: "Archivo Black", sans-serif;
    font-size: 32px;
    color: var(--white);
  }
  .schedule .day { color: var(--yellow); }
  .time {
    position: absolute;
    left: 36px;
    top: 772px;
    margin: 0;
    font-family: "Archivo Black", sans-serif;
    font-size: 50px;
    color: var(--yellow);
  }
  .time .hour { color: var(--red); }
  .offer {
    position: absolute;
    left: 10px;
    top: 870px;
    width: 216px;
    height: 216px;
    border-radius: 50%;
    background: var(--yellow);
    display: flex;
    flex-direction: column;
    align-items: center;
    justify-content: center;
    text-align: center;
    font-family: "Archivo Black", sans-serif;
    color: var(--dark);
    line-height: 1;
  }
  .offer::before {
    content: "";
    position: absolute;
    inset: 8px;
    border-radius: 50%;
    border: 3px dotted var(--red);
  }
  .offer-line { font-size: 19px; }
  .offer-free { font-size: 40px; margin: 2px 0 0; }
  .offer-trial { font-size: 20px; color: var(--red); }
  .offer-call { font-size: 22px; margin-top: 4px; }
  .phone {
    position: absolute;
    left: 200px;
    top: 955px;
    display: flex;
    align-items: center;
    gap: 14px;
    font-family: "Roboto Condensed", sans-serif;
    font-weight: 700;
    font-size: 30px;
    color: var(--dark);
  }
  .map {
    position: absolute;
    left: 600px;
    top: 777px;
    width: 189px;
    height: 144px;
    border: 4px solid var(--red);
    background: linear-gradient(135deg, var(--map-fill), #f3efe2 60%, #d6e6c8);
  }
  .address {
    position: absolute;
    right: 47px;
    top: 938px;
    margin: 0;
    text-align: right;
    font-family: "Arimo", sans-serif;
    font-size: 24px;
    line-height: 34px;
    color: var(--white);
    font-style: normal;
  }
  .address svg { vertical-align: -3px; margin-right: 4px; }
  .social {
    position: absolute;
    left: 626px;
    top: 1034px;
    display: flex;
    gap: 12px;
  }
  .social-dot {
    width: 48px;
    height: 48px;
    border-radius: 50%;
    background: #3d8fc9;
  }
  .social-dot.dark-blue { background: #1f5e8c; }
  .social-dot.red { background: #c9382c; }
</style>
</head>
<body>
  <main class="flyer">
    <svg class="flyer-shapes" width="850" height="1105" viewBox="0 0 850 1105">
      <defs>
        <linearGradient id="photo-tone" x1="0" y1="0" x2="1" y2="1">
          <stop offset="0" stop-color="var(--photo-light)"/>
          <stop offset="1" stop-color="var(--photo-mid)"/>
        </linearGradient>
      </defs>
      <rect x="0" y="0" width="850" height="600" fill="url(#photo-tone)" role="img" aria-label="Photo of four children in white martial arts uniforms with black and red belts, standing in ready stance"/>
      <polygon points="0,82 710,598 850,598 850,1105 0,1105" fill="var(--dark)"/>
      <polygon points="0,65 625,565 0,565" fill="var(--red)"/>
      <polygon points="0,65 0,80 18,80" fill="var(--red)"/>
      <polygon points="630,595 700,595 655,650 600,650" fill="var(--red)"/>
      <polygon points="755,545 850,480 850,700 690,755 595,755" fill="var(--yellow)"/>
      <polygon points="755,545 850,480 850,520 755,600" fill="var(--orange)"/>
      <polygon points="750,555 850,525 850,620 750,715" fill="var(--red)"/>
      <polygon points="850,620 850,700 690,755 750,715" fill="var(--orange)"/>
      <polygon points="190,932 488,932 420,1015 190,1015" fill="var(--yellow)"/>
      <polygon points="400,1025 600,1025 530,1105 340,1105" fill="var(--orange)"/>
      <polygon points="460,1025 600,1025 530,1105 430,1105" fill="var(--yellow)"/>
      <polygon points="420,1070 455,1070 455,1105 400,1105" fill="var(--red)"/>
    </svg>

    <div class="brand">
      <span class="brand-dot"></span>
      <span class="brand-name">KICKSTEADY</span>
    </div>

    <h1 class="headline">
      <span class="headline-small">Children’s</span>
      <span class="headline-big">MARTIAL</span>
      <span class="headline-mid">ART CLASSES</span>
    </h1>

    <p class="tagline">Fun and exciting yet<br>controlled and disciplined</p>

    <p class="schedule"><span class="day">Tuesday’s</span> And <span class="day">Thursday’s</span></p>
    <p class="time">TIME- <span class="hour">6pm</span></p>

    <div class="offer">
      <span class="offer-line">BOOK A</span>
      <span class="offer-free">FREE</span>
      <span class="offer-trial">TRIAL CLASS</span>
      <span class="offer-call">CALL NOW</span>
    </div>

    <div class="phone">
      <svg width="36" height="36" viewBox="0 0 24 24" aria-hidden="true">
        <path d="M6.6 10.8c1.4 2.8 3.8 5.1 6.6 6.6l2.2-2.2c.3-.3.7-.4 1-.2 1.1.4 2.3.6 3.6.6.6 0 1 .4 1 1V20c0 .6-.4 1-1 1C10.6 21 3 13.4 3 4c0-.6.4-1 1-1h3.5c.6 0 1 .4 1 1 0 1.3.2 2.5.6 3.6.1.3 0 .7-.2 1L6.6 10.8z" fill="var(--dark)"/>
        <path d="M15 3a6 6 0 0 1 6 6M15 6a3 3 0 0 1 3 3" stroke="var(--dark)" stroke-width="1.6" fill="none"/>
      </svg>
      <span>0400 123 456</span>
    </div>

    <div class="map" role="img" aria-label="Street map of the surrounding suburbs with a marker at the class location"></div>

    <address class="address">
      <svg width="22" height="22" viewBox="0 0 24 24" aria-hidden="true">
        <circle cx="12" cy="12" r="10.5" stroke="var(--white)" stroke-width="1.6" fill="none"/>
        <path d="M12 5.5a4 4 0 0 0-4 4c0 3 4 8 4 8s4-5 4-8a4 4 0 0 0-4-4z" fill="var(--white)"/>
        <circle cx="12" cy="9.5" r="1.5" fill="var(--dark)"/>
      </svg>12/48 Harbour Lane<br>Riverton VIC 3099
    </address>

    <div class="social">
      <span class="social-dot"></span>
      <span class="social-dot dark-blue"></span>
      <span class="social-dot red"></span>
    </div>
  </main>
</body>
</html>
```